New Business Card Design Project

Hi! I would like for you to design a business card for our aesthetic injections business. We offer Velmo, filler, skin care. I would like it to be elegant, feminine, modern and sleek/clean. I like black/gold foil/ivory/parchment colors. It can be either one or two sided. I would like matte black with gold foil logo on one side and ivory with gold foil information on the other side

Target Market(s)

target market is the discerning woman who wants to look her best

Industry/Entity Type

beauty

Contact Information for Business Card

logo, name, phone, email, website, instagram, facebook, location

Requirements
Must have
• logo and info
Nice to have
• the icons for cell, instagram, email, fb etc
Should not have
• images of people

```html
<!DOCTYPE html>
<html lang="en">
<head>
<meta charset="UTF-8">
<title>The Lumen Parlour – Business Card</title>
<link href="https://fonts.googleapis.com/css2?family=Arimo:wght@400;700&display=swap" rel="stylesheet">
<style>
  :root {
    --backdrop: #e6e6e6;
    --card-black: #151515;
    --gold: #c8ad62;
    --gold-edge: #9c8440;
  }
  * { margin: 0; padding: 0; box-sizing: border-box; }
  html, body {
    width: 1200px;
    height: 884px;
    overflow: hidden;
    background: var(--backdrop);
    font-family: "Arimo", Arial, sans-serif;
  }
  .card {
    position: absolute;
    left: 250px;
    width: 700px;
    height: 400px;
    background: var(--card-black);
    border: 2px solid var(--gold-edge);
    color: var(--gold);
  }
  .card--front { top: 20px; }
  .card--back { top: 464px; }

  .brand-mark {
    position: absolute;
    border: 1.5px solid var(--gold);
    border-radius: 50%;
    display: flex;
    align-items: center;
    justify-content: center;
    text-align: center;
  }
  .card--front .brand-mark { left: 86px; top: 64px; width: 214px; height: 214px; }
  .card--back .brand-mark { left: 224px; top: 74px; width: 250px; height: 250px; }

  .brand-name {
    font-weight: 400;
    letter-spacing: 3px;
    line-height: 1.35;
    color: var(--gold);
  }
  .card--front .brand-name { font-size: 21px; }
  .card--back .brand-name { font-size: 25px; }

  .divider {
    position: absolute;
    left: 350px;
    top: 84px;
    width: 1.5px;
    height: 182px;
    background: var(--gold);
  }
  .contact {
    position: absolute;
    left: 380px;
    top: 82px;
    font-size: 15px;
    line-height: 1.3;
  }
  .contact .person-name {
    font-weight: 700;
    font-size: 19px;
    letter-spacing: 0.5px;
  }
  .contact .person-role { font-size: 16px; margin-bottom: 18px; }
  .contact .address { margin-bottom: 6px; }
  .contact-line {
    display: flex;
    align-items: center;
    gap: 8px;
    height: 22px;
  }
  .contact-line svg { width: 14px; height: 14px; flex: none; }

  .social-row {
    position: absolute;
    left: 106px;
    bottom: 38px;
    display: flex;
    gap: 26px;
    font-size: 16px;
  }
  .social-item { display: flex; align-items: center; gap: 8px; }
  .social-badge {
    width: 14px;
    height: 14px;
    background: var(--gold);
    border-radius: 2px;
  }
</style>
</head>
<body>
  <section class="card card--front">
    <div class="brand-mark">
      <span class="brand-name">THE LUMEN<br>PARLOUR</span>
    </div>

    <div class="divider"></div>

    <div class="contact">
      <div class="person-name">MARCUS DELRAY</div>
      <div class="person-role">Operations Manager</div>
      <div class="address">48 Willow Crest Lane,<br>Maple Ridge, ON K2T 5R8</div>

      <div class="contact-line">
        <svg viewBox="0 0 24 24" aria-hidden="true"><path fill="var(--gold)" d="M6.6 10.8a15 15 0 0 0 6.6 6.6l2.2-2.2c.3-.3.7-.4 1-.2 1.1.4 2.3.6 3.6.6.6 0 1 .4 1 1V20c0 .6-.4 1-1 1A17 17 0 0 1 3 4c0-.6.4-1 1-1h3.5c.6 0 1 .4 1 1 0 1.3.2 2.5.6 3.6.1.3 0 .7-.2 1z"/></svg>
        <span>905-555-0142</span>
      </div>
      <div class="contact-line">
        <svg viewBox="0 0 24 24" aria-hidden="true"><rect x="2" y="5" width="20" height="14" fill="var(--gold)"/><path d="M2 5l10 8 10-8" fill="none" stroke="var(--card-black)" stroke-width="1.6"/></svg>
        <span>info@lumenparlour.ca</span>
      </div>
      <div class="contact-line">
        <svg viewBox="0 0 24 24" aria-hidden="true"><g fill="none" stroke="var(--gold)" stroke-width="2"><circle cx="12" cy="12" r="9"/><ellipse cx="12" cy="12" rx="4" ry="9"/><path d="M3 12h18"/></g></svg>
        <span>www.lumenparlour.ca</span>
      </div>
    </div>

    <div class="social-row">
      <div class="social-item"><span class="social-badge"></span><span>@thelumenparlour</span></div>
      <div class="social-item"><span class="social-badge"></span><span>@thelumenparlour</span></div>
    </div>
  </section>

  <section class="card card--back">
    <div class="brand-mark">
      <span class="brand-name">THE LUMEN<br>PARLOUR</span>
    </div>
  </section>
</body>
</html>
```